Branded Postcard Design for Physician Gift

We’re looking for a clean, professional, and slightly playful postcard design to include inside branded Brevard tumblers being sent to physicians participating in a clinical pilot study.

The card should incorporate our KOR LUMEN TX logo and brand colors (magenta and navy — logo attached), and prominently feature the quote:

“Here’s to staying hydrated as we sprint to the finish line!”

We’d love a design that feels modern and clean — appropriate for a physician audience — with a subtle nod to hydration and the idea of approaching the study’s finish line (e.g., a small water droplet, a minimalist finish line/checkered flag, etc.).

Specs:

Size: Standard postcard (horizontal or vertical layout is fine)

Front: Main quote with design elements

Back: Optional space for a short thank-you message (can be left blank or designed with placeholder text)

Tone:
Professional but friendly, clean and visually appealing with minimal clutter.

I am totally open to your creative ideas - you do not need to follow this description exactly! I'd love to see your ideas. :)

```html
<!DOCTYPE html>
<html lang="en">
<head>
<meta charset="utf-8">
<title>KOR LUMEN TX – Physician Postcard</title>
<link rel="stylesheet" href="https://fonts.googleapis.com/css2?family=Kaushan+Script&display=swap">
<style>
  :root {
    --magenta: #a312f2;
    --navy: #0c0f4b;
    --card: #ffffff;
    --backdrop: #ecebe7;
    --droplet-light: #f7f7f7;
    --droplet-mid: #e3e4e6;
    --script: "Kaushan Script", cursive;
  }
  * { box-sizing: border-box; margin: 0; padding: 0; }
  html, body {
    width: 1200px;
    height: 1200px;
    overflow: hidden;
    background: var(--backdrop);
  }
  .canvas {
    width: 1200px;
    height: 1200px;
    display: flex;
    flex-direction: column;
    align-items: center;
    justify-content: center;
    gap: 60px;
  }
  .postcard {
    position: relative;
    width: 780px;
    height: 520px;
    background: var(--card);
    box-shadow: 0 10px 28px rgba(0, 0, 0, 0.18);
    overflow: hidden;
  }
  .postcard__droplets {
    position: absolute;
    left: 0;
    right: 0;
    bottom: 0;
    height: 58%;
    background:
      radial-gradient(ellipse at 30% 60%, var(--droplet-mid) 0%, transparent 55%),
      radial-gradient(ellipse at 70% 40%, var(--droplet-mid) 0%, transparent 50%),
      linear-gradient(to bottom, var(--card) 0%, var(--droplet-light) 35%, var(--droplet-light) 100%);
    opacity: 0.9;
  }
  .postcard__shapes {
    position: absolute;
    inset: 0;
    width: 100%;
    height: 100%;
  }
  .shape--magenta { fill: var(--magenta); }
  .shape--navy { fill: var(--navy); }

  .brand {
    position: absolute;
    font-family: var(--script);
    font-weight: 400;
    color: var(--navy);
    white-space: nowrap;
    line-height: 1;
  }
  .postcard--front .brand {
    left: 62px;
    top: 92px;
    font-size: 76px;
  }
  .postcard--back .brand {
    left: 92px;
    top: 44px;
    font-size: 34px;
  }

  .quote {
    position: absolute;
    left: 70px;
    top: 290px;
    font-family: var(--script);
    font-size: 35px;
    line-height: 1.5;
    color: var(--navy);
    transform: rotate(-4deg);
    transform-origin: left top;
  }
</style>
</head>
<body>
<main class="canvas">

  <section class="postcard postcard--back" aria-label="Postcard back">
    <div class="postcard__droplets" role="img" aria-label="Soft water droplets pattern"></div>
    <svg class="postcard__shapes" viewBox="0 0 780 520" aria-hidden="true">
      <path class="shape--magenta" d="M0 120 H20 Q32 120 32 132 V283 Q32 295 20 295 H0 Z"/>
      <path class="shape--navy" d="M0 315 H20 Q32 315 32 327 V520 H0 Z"/>
    </svg>
    <p class="brand">KOR LUMEN TX</p>
  </section>

  <section class="postcard postcard--front" aria-label="Postcard front">
    <div class="postcard__droplets" role="img" aria-label="Soft water droplets pattern"></div>
    <svg class="postcard__shapes" viewBox="0 0 780 520" aria-hidden="true">
      <path class="shape--magenta" d="M700 0 H780 V262 L642 238 Q622 234 628 214 Z"/>
      <path class="shape--navy" d="M780 286 L632 258 Q614 255 609 274 L540 520 H780 Z"/>
    </svg>
    <p class="brand">KOR LUMEN TX</p>
    <p class="quote">Here’s to staying hydrated<br>as we sprint to the finish line!</p>
  </section>

</main>
</body>
</html>
```